Corroway Medical Imaging marketing poster

A poster to advertise our services. Something outstanding that catches the eye. Will be displayed at medical centres. Needs to advertise the following:
Opening hours - Mon-fri 8am-5:30pm Sat 8am-12:30
Services offered: Ultrasound, CT, Xray, Conebeam CT, Barium Studies, Injections and Biopsies, 3D/4D pregnancy scans.
We Bulk Bill concession card holders and under 18's
Locally owned and operated
www.corrowaymedicalimaging.example.au
include contact details also Tel: 96384027 Fax: 9638 4093

```html
<!DOCTYPE html>
<html lang="en">
<head>
<meta charset="utf-8">
<title>Corroway Medical Imaging – Services Poster</title>
<link href="https://fonts.googleapis.com/css2?family=Source+Sans+3:ital,wght@0,400;0,600;0,700;1,400;1,600&display=swap" rel="stylesheet">
<style>
  :root {
    --backdrop: #d4d5d7;
    --paper: #ffffff;
    --sky-blue: #55a7dc;
    --edge-blue: #a9d6f0;
    --lime: #a8c939;
    --ink-grey: #55585b;
    --white: #ffffff;
    --list-text: #eaf4fb;
    --wall-blue: #cfe4ee;
    --wall-light: #eef3f4;
    --coat-white: #f7f6f3;
    --device-grey: #c9d0d3;
    --screen-navy: #33477a;
  }
  * { margin: 0; padding: 0; box-sizing: border-box; }
  html, body { width: 932px; height: 1200px; overflow: hidden; }
  body {
    background: var(--backdrop);
    font-family: "Source Sans 3", sans-serif;
    position: relative;
  }
  .poster {
    position: absolute;
    left: 102px; top: 76px;
    width: 726px; height: 1028px;
    background: var(--paper);
    overflow: hidden;
  }
  .poster-shapes { position: absolute; inset: 0; }

  .brand {
    position: absolute;
    left: 48px; top: 516px;
    display: flex; align-items: center; gap: 14px;
  }
  .brand-dot {
    width: 14px; height: 14px; border-radius: 50%;
    background: var(--sky-blue);
  }
  .brand-name {
    color: var(--ink-grey);
    font-weight: 400;
    line-height: 1;
  }
  .brand-name .line-main { display: block; font-size: 56px; letter-spacing: 1px; }
  .brand-name .line-sub { display: block; font-size: 28px; letter-spacing: 1px; margin-top: 4px; }

  .services-tab {
    position: absolute;
    left: 403px; top: 666px;
    width: 330px; height: 42px;
    background: var(--lime);
    border-radius: 21px 0 0 21px;
    color: var(--white);
    font-weight: 700;
    font-size: 25px;
    text-align: right;
    padding-right: 36px;
    line-height: 42px;
  }
  .service-list {
    position: absolute;
    right: 26px; top: 711px;
    list-style: none;
  }
  .service-list li {
    display: flex; justify-content: flex-end; align-items: center;
    height: 34px;
    color: var(--list-text);
    font-weight: 600;
    font-size: 21px;
    letter-spacing: 0.2px;
  }
  .service-list svg { margin-left: 14px; flex: none; }

  .practice-info {
    position: absolute;
    left: 0; top: 746px;
    width: 372px;
    text-align: center;
    color: var(--white);
  }
  .practice-name { font-size: 21px; font-weight: 600; line-height: 28px; }
  .practice-tagline { font-size: 15.5px; line-height: 22px; }
  .hours-title { font-size: 20px; font-weight: 600; margin-top: 22px; line-height: 26px; }
  .hours-text, .address { font-size: 15px; line-height: 21px; }
  .bulk-bill { font-size: 13.5px; font-style: italic; font-weight: 600; margin-top: 22px; }

  .contact-footer {
    position: absolute;
    left: 0; top: 966px;
    width: 726px; height: 62px;
    color: var(--white);
  }
  .contact-lines {
    position: absolute; left: 18px; top: 3px;
    list-style: none;
    font-size: 13px; font-weight: 600;
  }
  .contact-lines li { display: flex; align-items: center; height: 18px; }
  .contact-lines svg { margin-right: 7px; }
  .website {
    position: absolute; right: 44px; top: 26px;
    font-size: 16px; font-weight: 600;
  }
</style>
</head>
<body>
  <main class="poster">
    <svg class="poster-shapes" width="726" height="1028" viewBox="0 0 726 1028">
      <defs>
        <linearGradient id="photo-tone" x1="0" y1="0" x2="1" y2="0.9">
          <stop offset="0" stop-color="var(--wall-blue)"/>
          <stop offset="0.3" stop-color="var(--wall-light)"/>
          <stop offset="0.5" stop-color="var(--coat-white)"/>
          <stop offset="0.72" stop-color="var(--device-grey)"/>
          <stop offset="1" stop-color="var(--screen-navy)"/>
        </linearGradient>
      </defs>
      <path class="photo-area" role="img" aria-label="Photograph of a sonographer in a white blouse operating an ultrasound machine with a scan shown on its monitor"
            d="M0,0 H726 V588 C520,575 250,470 0,228 Z" fill="url(#photo-tone)"/>
      <path class="photo-edge" d="M0,228 C250,470 520,575 726,588" fill="none" stroke="var(--edge-blue)" stroke-width="3"/>
      <path class="wave-edge" d="M0,752 C120,652 350,610 726,606 V616 C350,620 120,662 0,760 Z" fill="var(--edge-blue)"/>
      <path class="info-band" d="M0,760 C120,662 350,620 726,616 V966 H0 Z" fill="var(--sky-blue)"/>
      <rect class="footer-band" x="0" y="966" width="726" height="62" fill="var(--lime)"/>
    </svg>

    <div class="brand">
      <span class="brand-dot"></span>
      <div class="brand-name">
        <span class="line-main">CORROWAY</span>
        <span class="line-sub">MEDICAL IMAGING</span>
      </div>
    </div>

    <div class="services-tab">SERVICES OFFERED</div>
    <ul class="service-list">
      <li>ULTRASOUND<svg width="18" height="18" viewBox="0 0 18 18"><circle cx="9" cy="9" r="8.5" fill="var(--lime)"/><path d="M10.5,5 L6.5,9 L10.5,13" stroke="var(--sky-blue)" stroke-width="2.2" fill="none"/></svg></li>
      <li>CT<svg width="18" height="18" viewBox="0 0 18 18"><circle cx="9" cy="9" r="8.5" fill="var(--lime)"/><path d="M10.5,5 L6.5,9 L10.5,13" stroke="var(--sky-blue)" stroke-width="2.2" fill="none"/></svg></li>
      <li>XRAY<svg width="18" height="18" viewBox="0 0 18 18"><circle cx="9" cy="9" r="8.5" fill="var(--lime)"/><path d="M10.5,5 L6.5,9 L10.5,13" stroke="var(--sky-blue)" stroke-width="2.2" fill="none"/></svg></li>
      <li>CONEBEAM CT<svg width="18" height="18" viewBox="0 0 18 18"><circle cx="9" cy="9" r="8.5" fill="var(--lime)"/><path d="M10.5,5 L6.5,9 L10.5,13" stroke="var(--sky-blue)" stroke-width="2.2" fill="none"/></svg></li>
      <li>BARIUM STUDIES<svg width="18" height="18" viewBox="0 0 18 18"><circle cx="9" cy="9" r="8.5" fill="var(--lime)"/><path d="M10.5,5 L6.5,9 L10.5,13" stroke="var(--sky-blue)" stroke-width="2.2" fill="none"/></svg></li>
      <li>INJECTIONS AND BIOPSIES<svg width="18" height="18" viewBox="0 0 18 18"><circle cx="9" cy="9" r="8.5" fill="var(--lime)"/><path d="M10.5,5 L6.5,9 L10.5,13" stroke="var(--sky-blue)" stroke-width="2.2" fill="none"/></svg></li>
      <li>3D/4D PREGNANCY SCANS<svg width="18" height="18" viewBox="0 0 18 18"><circle cx="9" cy="9" r="8.5" fill="var(--lime)"/><path d="M10.5,5 L6.5,9 L10.5,13" stroke="var(--sky-blue)" stroke-width="2.2" fill="none"/></svg></li>
    </ul>

    <section class="practice-info">
      <h1 class="practice-name">CORROWAY MEDICAL IMAGING</h1>
      <p class="practice-tagline">Locally owned and Operated</p>
      <h2 class="hours-title">Opening Hours</h2>
      <p class="hours-text">Mon-fri 8am-5:30pm Sat 8am-12:30</p>
      <p class="address">14/2 Larkfield Dr, Corroway WA 6231</p>
      <p class="bulk-bill">We Bulk Bill concession card holders and under 18's</p>
    </section>

    <footer class="contact-footer">
      <ul class="contact-lines">
        <li><svg width="12" height="10" viewBox="0 0 12 10"><path d="M1,3 C1,1 11,1 11,3 L9,4 L8,2.5 H4 L3,4 Z M2,9 L3.5,5 H8.5 L10,9 Z" fill="var(--white)"/></svg>08 9638 4027</li>
        <li><svg width="12" height="11" viewBox="0 0 12 11"><rect x="3" y="0.5" width="6" height="3.5" fill="none" stroke="var(--white)"/><rect x="0.5" y="4" width="11" height="5" fill="var(--white)"/><rect x="3" y="7" width="6" height="3.5" fill="var(--lime)" stroke="var(--white)"/></svg>08 9638 4093</li>
        <li><svg width="12" height="9" viewBox="0 0 12 9"><rect x="0.5" y="0.5" width="11" height="8" fill="var(--white)"/><path d="M0.5,0.5 L6,5 L11.5,0.5" stroke="var(--lime)" fill="none"/></svg>info@corrowaymedicalimaging.example.au</li>
      </ul>
      <p class="website">www.corrowaymedicalimaging.example.au</p>
    </footer>
  </main>
</body>
</html>
```